Bounty Bazaar 2022- FB poster ads

Design for our Bounty Bazaar Event
Designs 3 designs for Face Book Banner, posts and social Media ads
Each can look the same just different subjects on each
1. Design We're Back!
The Bounty Bazaar Is Back!
Ventura County’s Premier Food, Wine and Brew Event
August 14th
Vendor and ticket info at https://bountybazaarhub.com/

2. Vendors be a part of the event
The Bounty Bazaar is Back!
August 14th 2020
Vendors sign up today at
Vendor info at https://bountybazaarhub.com/

3. Sponsor info
The Bounty Bazaar
August 14th 2022
Check out our great Sponsorship opportunities
Sponsor info at https://bountybazaarhub.com/

Target Market(s)

Foodies, wine and beer enthusists

Industry/Entity Type

Farm to fork, fresh in season and local

Colors
00AB8E
00BBA5
67D7C9
C6EFE9
E9F9F6

Requirements
Should not have
• no fast food looking photos

```html
<!DOCTYPE html>
<html lang="en">
<head>
<meta charset="utf-8">
<title>Bounty Bazaar – Vendor Banner</title>
<link rel="stylesheet" href="https://fonts.googleapis.com/css2?family=Lobster&display=swap">
<style>
  :root {
    --stage: #8c8c8c;
    --parchment-light: #f1dcaa;
    --parchment-mid: #e2bf80;
    --parchment-dark: #c99b58;
    --teal: #00ab8e;
    --teal-deep: #009a80;
    --brown: #6f3f2f;
    --brown-shadow: rgba(60, 30, 18, 0.35);
    --frame: #7a4a2c;
    --white: #ffffff;
    --food-dark: #3d3a38;
    --food-mid: #8a6a52;
    --food-light: #d9b98a;
  }
  * { margin: 0; padding: 0; box-sizing: border-box; }
  html, body { width: 1200px; height: 944px; overflow: hidden; }
  body { background: var(--stage); position: relative; font-family: 'Lobster', cursive; }

  .banner {
    position: absolute; left: 0; top: 157px; width: 1200px; height: 629px;
    overflow: hidden;
    background:
      radial-gradient(ellipse at 30% 30%, var(--parchment-light) 0%, var(--parchment-mid) 60%, var(--parchment-dark) 100%);
  }

  .teal-band {
    position: absolute; left: 0; top: 303px; width: 1200px; height: 310px;
    background: var(--teal);
  }

  .headline {
    position: absolute; left: 40px; top: 30px; width: 500px;
    text-align: center; color: var(--brown);
    text-shadow: 3px 3px 0 var(--brown-shadow);
    line-height: 1;
  }
  .headline .the { display: block; font-size: 62px; padding-left: 70px; }
  .headline .big { display: block; font-size: 112px; margin-top: -10px; }
  .headline .rest { display: block; font-size: 60px; margin-top: -4px; }

  .event-copy {
    position: absolute; left: 50px; top: 348px; width: 470px;
    color: var(--white); text-align: center;
    text-shadow: 2px 2px 0 rgba(0, 80, 66, 0.45);
    line-height: 1.15;
  }
  .event-copy .lead { font-size: 22px; text-align: left; padding-left: 20px; }
  .event-copy .title { font-size: 42px; margin-top: 10px; }
  .event-copy .date { font-size: 42px; }

  .vendor-call {
    position: absolute; right: 688px; top: 508px;
    color: var(--white); text-align: right; font-size: 25px; line-height: 1.12;
    text-shadow: 2px 2px 0 rgba(0, 80, 66, 0.45);
    white-space: nowrap;
  }

  .photo-frame {
    position: absolute; left: 560px; top: 150px; width: 612px; height: 410px;
    border: 7px solid var(--frame); border-radius: 46px;
    box-shadow: 0 6px 0 var(--teal-deep);
    overflow: hidden;
  }
  .photo-frame .photo {
    width: 100%; height: 100%;
    background:
      radial-gradient(ellipse at 62% 45%, var(--food-light) 0%, var(--food-mid) 45%, var(--food-dark) 100%);
  }

  .brand-name {
    position: absolute; left: 668px; top: 72px; width: 400px;
    text-align: center; font-size: 34px; color: var(--brown);
  }
</style>
</head>
<body>
  <main class="banner">
    <div class="teal-band"></div>

    <h1 class="headline">
      <span class="the">The</span>
      <span class="big">Bounty</span>
      <span class="rest">Bazaar Is Back!</span>
    </h1>

    <div class="event-copy">
      <p class="lead">Ventura County’s Premier Food,</p>
      <p class="title">Wine and Brew Event</p>
      <p class="date">August 14th 2022</p>
    </div>

    <p class="vendor-call">Vendors sign up today at<br>at https://bountybazaarhub.com/</p>

    <div class="photo-frame">
      <div class="photo" role="img" aria-label="Photo of sliced bread rounds topped with pâté and parsley in a serving bowl"></div>
    </div>

    <p class="brand-name">Bounty Bazaar Hub</p>
  </main>
</body>
</html>
```